Business Cards for a Firearms Business - Quorvane Works

Quorvane Works manufactures, distributes and retails firearms parts. I am looking for someone to use the logos that I have provided to design some business cards that show that we're a modern, industrial, design focused and tactical business.

These will be a standard business card on standard cardstock paper. Nothing special here about the dimensions or materials.

On the front of the card, use either the logos that I am providing, or do some slight modifications to these logos to fit the design that looks the best. Feel free to pick the one that you like, or that will fit what you're trying to do the best here. Take artistic liberty to make this card pop. I do not want any contact information on the front of the card, only the company logo.

On the back of the card I would like the contact information. Please use fictitious contact information for now, and make the background look cool somehow.

```html
<!DOCTYPE html>
<html lang="en">
<head>
<meta charset="utf-8">
<title>Quorvane Works – Business Cards</title>
<link href="https://fonts.googleapis.com/css2?family=Open+Sans:wght@400;800&family=PT+Serif:wght@400;700&display=swap" rel="stylesheet">
<style>
  :root {
    --backdrop: #e9e6e1;
    --card-orange: #f28c1e;
    --logo-ink: #353434;
    --nav-dark: #2f2f31;
    --nav-active: #5a5a5d;
    --nav-divider: #c77418;
    --contact-ink: #ffffff;
  }
  * { margin: 0; padding: 0; box-sizing: border-box; }
  html, body { width: 1200px; height: 900px; overflow: hidden; }
  body {
    background: var(--backdrop);
    display: flex;
    flex-direction: column;
    align-items: center;
    justify-content: center;
    gap: 40px;
  }
  .card {
    position: relative;
    width: 700px;
    height: 400px;
    background: var(--card-orange);
    box-shadow: 0 6px 18px rgba(0,0,0,0.18);
    overflow: hidden;
  }
  .wordmark {
    font-family: "Open Sans", sans-serif;
    font-weight: 800;
    color: var(--logo-ink);
    text-transform: uppercase;
    line-height: 1;
    text-align: center;
  }
  .card-front { display: flex; align-items: center; justify-content: center; }
  .card-front .wordmark { font-size: 60px; letter-spacing: 8px; }
  .card-front .wordmark span { display: block; }
  .card-front .wordmark span + span { margin-top: 10px; }

  .main-nav {
    position: absolute;
    top: 44px; left: 0; right: 0;
    height: 40px;
    background: var(--nav-dark);
    display: flex;
  }
  .main-nav .nav-item {
    font-family: "Open Sans", sans-serif;
    font-size: 17px;
    color: #fff;
    text-transform: uppercase;
    padding: 0 26px;
    display: flex;
    align-items: center;
    border-right: 3px solid var(--nav-divider);
  }
  .main-nav .nav-item:first-child { padding-left: 40px; }
  .main-nav .nav-item.is-active { background: var(--nav-active); border-right: none; }

  .card-back .wordmark {
    position: absolute;
    left: 40px; top: 180px;
    font-size: 36px;
    letter-spacing: 5px;
    text-align: left;
  }
  .card-back .wordmark span { display: block; }
  .card-back .wordmark span + span { margin-top: 6px; margin-left: 28px; }

  .contact {
    position: absolute;
    left: 440px; top: 118px;
    font-family: "PT Serif", serif;
    color: var(--contact-ink);
  }
  .contact .person-name { font-size: 22px; font-weight: 700; }
  .contact .person-title { font-size: 15px; margin-top: 2px; }
  .contact-list { list-style: none; margin-top: 36px; }
  .contact-list li {
    display: flex; align-items: center; gap: 10px;
    font-size: 16px; line-height: 26px;
  }
  .contact-list svg { width: 16px; height: 16px; flex: none; }
</style>
</head>
<body>
  <section class="card card-front" aria-label="Card front">
    <div class="wordmark"><span>Quorvane</span><span>Works</span></div>
  </section>

  <section class="card card-back" aria-label="Card back">
    <nav class="main-nav">
      <div class="nav-item">Home</div>
      <div class="nav-item">Forum</div>
      <div class="nav-item">Portfolio</div>
      <div class="nav-item is-active">Contact</div>
    </nav>

    <div class="wordmark"><span>Quorvane</span><span>Works</span></div>

    <div class="contact">
      <div class="person-name">Prename Name</div>
      <div class="person-title">Creative Director</div>
      <ul class="contact-list">
        <li>
          <svg viewBox="0 0 16 16" fill="none" stroke="#fff" stroke-width="1.4"><path d="M2 7 L8 2 L14 7 V14 H2 Z"/><rect x="6.5" y="9" width="3" height="5"/></svg>
          Your address here
        </li>
        <li>
          <svg viewBox="0 0 16 16" fill="#fff"><path d="M4 1.5 L6.5 4.5 L5 6.5 C6 8.5 7.5 10 9.5 11 L11.5 9.5 L14.5 12 L12.5 14.5 C7 14 2 9 1.5 3.5 Z"/></svg>
          +61 100 555 010
        </li>
        <li>
          <svg viewBox="0 0 16 16" fill="none" stroke="#fff" stroke-width="1.4"><rect x="1.5" y="3.5" width="13" height="9"/><path d="M1.5 3.5 L8 9 L14.5 3.5"/></svg>
          name@company
        </li>
        <li>
          <svg viewBox="0 0 16 16" fill="none" stroke="#fff" stroke-width="1.3"><circle cx="8" cy="8" r="6.5"/><ellipse cx="8" cy="8" rx="3" ry="6.5"/><path d="M1.5 8 H14.5"/></svg>
          www.quorvaneworks.com.au
        </li>
      </ul>
    </div>
  </section>
</body>
</html>
```